Cedar Club Food Flyer Postcard

Want a two sided postcard (6x11 quillmark, template attached) designed to be used with TWRK CNPA. The Cedars serves food on Sundays (5-8pm) and Mondays (5-9pm). A menu and other graphics are attached, no need to use all of them. Also want two coupons in the card, $2 dollars off any sandwich, and $2 off any appetizer.

```html
<!DOCTYPE html>
<html lang="en">
<head>
<meta charset="utf-8">
<title>Cedar Club Food Flyer Postcard</title>
<link rel="stylesheet" href="https://fonts.googleapis.com/css2?family=Alfa+Slab+One&family=Baloo+2:wght@700;800&family=Bangers&family=Kaushan+Script&family=Nunito:wght@700;800&family=Oswald:wght@700&display=swap">
<style>
:root{
  --red:#d3213f;
  --blue:#1b4f9c;
  --navy:#173f86;
  --yellow:#f9bd1b;
  --cream:#efe9df;
  --white:#ffffff;
  --page:#e4e4e4;
  --ink:#1d2a44;
}
*{margin:0;padding:0;box-sizing:border-box}
html,body{width:1089px;height:1200px;overflow:hidden;background:var(--page)}
body{position:relative;font-family:"Nunito",sans-serif}
.card{position:absolute;left:136px;width:817px;height:446px;overflow:hidden;box-shadow:0 6px 18px rgba(0,0,0,.25)}
.card--front{top:125px;background:var(--cream)}
.card--back{top:634px;background:var(--white)}
.abs{position:absolute}
.photo{position:absolute;border-radius:50%;border:5px solid var(--yellow)}
.dot{position:absolute;border-radius:50%}

/* front */
.hero-photo{position:absolute;left:0;top:0;width:400px;height:446px}
.brand{left:412px;top:38px;width:76px;height:76px;border-radius:50%;border:3px solid var(--blue);background:var(--white);display:flex;align-items:center;justify-content:center;text-align:center;font-family:"Baloo 2",sans-serif;font-weight:800;font-size:14px;line-height:1;color:var(--blue)}
.title{left:522px;top:36px;font-family:"Baloo 2",sans-serif;font-weight:800;font-size:24px;color:var(--red);white-space:nowrap}
.phone-band{left:526px;top:71px;width:245px;height:31px;background:var(--blue);border-radius:3px 14px 3px 14px;transform:rotate(-1deg);display:flex;align-items:center;justify-content:center;gap:6px;font-family:"Baloo 2",sans-serif;font-weight:800;font-size:24px;color:var(--white)}
.rule{height:1px;background:var(--blue)}
.serving{left:540px;top:116px;width:220px;text-align:center;font-family:"Kaushan Script",cursive;font-size:19px;color:var(--red)}
.menu-head{top:158px;height:27px;display:flex;align-items:center;justify-content:center;font-family:"Kaushan Script",cursive;font-size:18px;border-radius:2px 10px 2px 10px;transform:rotate(-1deg)}
.menu-head--apps{left:403px;width:147px;background:var(--red);color:var(--white)}
.menu-head--burgers{left:584px;width:197px;background:var(--yellow);color:var(--navy)}
.divider{left:569px;top:160px;width:1px;height:249px;background:var(--red)}
.menu{position:absolute;list-style:none}
.menu li{display:flex;justify-content:space-between;align-items:center;font-family:"Bangers",cursive;font-size:12.5px;letter-spacing:.6px;color:var(--blue);white-space:nowrap}
.price{font-family:"Nunito",sans-serif;font-weight:800;font-size:10.5px;letter-spacing:0;padding:1px 6px 1px 14px;border-radius:0 9px 9px 0}
.menu--apps{left:402px;top:190px;width:148px}
.menu--apps li{height:28.6px}
.menu--apps .price{background:linear-gradient(90deg,transparent,var(--yellow) 30%);color:var(--ink)}
.menu--burgers{left:588px;top:192px;width:195px}
.menu--burgers li{height:21.5px}
.menu--burgers .price{background:linear-gradient(90deg,transparent,var(--red) 30%);color:var(--white)}
.note{left:386px;top:395px;width:180px;font-size:7.5px;line-height:1.3;color:var(--blue)}
.addons{left:588px;top:397px;font-size:10px;color:var(--blue)}
.addons b{color:var(--red);font-weight:700}
.fine{left:714px;top:416px;font-size:5px;color:var(--ink)}

/* back */
.label{position:absolute;left:48px;width:114px;height:26px;background:var(--red);border-radius:2px 10px 2px 10px;transform:rotate(-1deg);display:flex;align-items:center;justify-content:center;font-family:"Kaushan Script",cursive;font-size:18px;color:var(--white)}
.hours{position:absolute;left:24px;width:160px;text-align:center;font-weight:800;font-size:11px;line-height:17px;color:var(--white)}
.club-name{left:34px;top:303px;font-weight:800;font-size:13px;color:var(--white)}
.address{left:55px;top:333px;font-weight:800;font-size:11px;line-height:14px;color:var(--white)}
.pin{left:40px;top:333px}
.back-phone{left:19px;top:388px;width:172px;height:27px;background:var(--yellow);border-radius:3px 12px 3px 12px;transform:rotate(-1deg);display:flex;align-items:center;justify-content:center;gap:4px;font-family:"Baloo 2",sans-serif;font-weight:800;font-size:18px;color:var(--ink)}
.coupon{position:absolute;left:387px;width:132px;height:61px;border:1.5px dashed var(--ink);display:flex;flex-direction:column;align-items:center;padding-top:8px}
.coupon-off{width:113px;height:24px;background:var(--red);border:2px solid var(--yellow);display:flex;align-items:center;justify-content:center;font-family:"Alfa Slab One",serif;font-size:17px;color:var(--white)}
.coupon-item{font-family:"Oswald",sans-serif;font-weight:700;font-size:16px;line-height:22px;color:var(--blue);letter-spacing:.3px}
.scissors{position:absolute;right:-6px;top:-6px;font-size:10px;color:var(--ink);background:var(--white)}
.badges{left:404px;top:171px;width:100px;height:41px;border:1px solid #888;background:var(--white)}
.follow{left:390px;top:222px;width:130px;text-align:center;font-weight:800;font-size:8px;line-height:13px;color:var(--ink)}
.follow .url{color:var(--blue)}
.stamp{left:704px;top:39px;width:73px;height:73px;border:1px solid var(--ink)}
.addr-line{left:573px;width:203px;height:1px;background:var(--ink)}
</style>
</head>
<body>

<section class="card card--front" aria-label="Postcard front: menu">
  <svg class="hero-photo" viewBox="0 0 400 446" role="img" aria-label="Photo of a bacon cheeseburger on red checkered paper">
    <defs>
      <linearGradient id="heroTone" x1="0" y1="0" x2="1" y2="1">
        <stop offset="0" stop-color="#1b1512"/>
        <stop offset=".45" stop-color="#8a5a2b"/>
        <stop offset=".75" stop-color="#c9a36a"/>
        <stop offset="1" stop-color="#c23a3a"/>
      </linearGradient>
    </defs>
    <path d="M0 0H322C372 40 392 110 370 180L340 446H0Z" fill="url(#heroTone)"/>
    <path d="M322 0C374 38 398 112 372 182" fill="none" stroke="#f9bd1b" stroke-width="6"/>
  </svg>
  <div class="dot" style="left:309px;top:50px;width:26px;height:26px;background:#d3213f;opacity:.85"></div>
  <div class="dot" style="left:316px;top:79px;width:26px;height:26px;background:#f9bd1b;opacity:.7"></div>
  <div class="photo" role="img" aria-label="Photo of loaded gems with olives" style="left:300px;top:112px;width:86px;height:86px;background:radial-gradient(circle,#c9954a,#5a3a1c)"></div>
  <div class="photo" role="img" aria-label="Photo of a patty melt" style="left:267px;top:178px;width:112px;height:112px;background:radial-gradient(circle,#b77b3e,#3a2614)"></div>
  <div class="photo" role="img" aria-label="Photo of chicken tenders with fries and ranch" style="left:184px;top:248px;width:138px;height:138px;background:radial-gradient(circle,#e2d6c2,#b27a3c 55%,#c23a3a)"></div>
  <div class="photo" role="img" aria-label="Photo of a BLT sandwich with fries" style="left:22px;top:257px;width:172px;height:172px;background:radial-gradient(circle,#d9c49a,#8c6a3f 60%,#2a221c)"></div>
  <div class="dot" style="left:267px;top:412px;width:130px;height:60px;background:var(--red)"></div>
  <div class="dot" style="left:491px;top:434px;width:170px;height:40px;background:var(--blue)"></div>
  <div class="dot" style="left:660px;top:-18px;width:170px;height:44px;background:var(--yellow);transform:rotate(-6deg)"></div>
  <div class="dot" style="left:806px;top:300px;width:30px;height:120px;background:var(--red);opacity:.85"></div>

  <div class="abs brand">Cedar<br>Club</div>
  <h1 class="abs title">Fairbrook Cedar Club</h1>
  <div class="abs phone-band">
    <svg width="18" height="18" viewBox="0 0 24 24" aria-hidden="true"><circle cx="12" cy="12" r="10.5" fill="none" stroke="#fff" stroke-width="2"/><path d="M8.5 6.5l2 2.2-1.2 1.6a8 8 0 0 0 4.4 4.4l1.6-1.2 2.2 2-1.5 2c-4.6-.3-8.3-4-8.8-8.8z" fill="#fff"/></svg>
    402-555-0147
  </div>
  <div class="abs rule" style="left:540px;top:113px;width:220px"></div>
  <p class="abs serving">Now Serving Food!</p>
  <div class="abs rule" style="left:540px;top:145px;width:220px"></div>

  <h2 class="abs menu-head menu-head--apps">Appetizers</h2>
  <h2 class="abs menu-head menu-head--burgers">Burgers and More</h2>
  <div class="abs divider"></div>

  <ul class="menu menu--apps">
    <li>Cauliflower<span class="price">$6.00</span></li>
    <li>Gizzards<span class="price">$5.00</span></li>
    <li>Fried Mushrooms<span class="price">$6.25</span></li>
    <li>Pickle Chips<span class="price">$7.50</span></li>
    <li>Onion Petals<span class="price">$6.00</span></li>
    <li>Loaded Fries<span class="price">$7.50</span></li>
    <li>Loaded Gems<span class="price">$8.00</span></li>
  </ul>
  <ul class="menu menu--burgers">
    <li>Hamburger<span class="price">$6.50</span></li>
    <li>Cheeseburger<span class="price">$7.00</span></li>
    <li>Bacon Cheeseburger<span class="price">$8.50</span></li>
    <li>Pizza Burger<span class="price">$6.00</span></li>
    <li>BLT<span class="price">$6.00</span></li>
    <li>Grilled Chicken Sandwich<span class="price">$7.00</span></li>
    <li>Patty Melt<span class="price">$7.50</span></li>
    <li>Chicken Tenders<span class="price">$7.75</span></li>
    <li>Grilled Cheese<span class="price">$4.00</span></li>
  </ul>
  <p class="abs note">Loaded includes pulled pork, nacho cheese, jalapeno &amp; black olives</p>
  <p class="abs addons">Add Fries <b>$2.50</b> or Add Gems <b>$2.75</b></p>
  <p class="abs fine">*Prices subject to change.</p>
</section>

<section class="card card--back" aria-label="Postcard back: hours, coupons and mailing area">
  <svg class="abs" style="left:0;top:0" width="360" height="446" viewBox="0 0 360 446" aria-hidden="true">
    <path d="M0 0H262C330 60 345 190 262 258C190 300 90 270 0 250Z" fill="#1b4f9c"/>
    <circle cx="108" cy="349" r="118" fill="#d3213f"/>
  </svg>
  <div class="label" style="top:39px">Grill Open</div>
  <p class="hours" style="top:71px">Dine-In or Carry-Out<br>Sundays 4pm-8pm<br>Mondays 5pm-9pm</p>
  <div class="label" style="top:141px">Bar Open</div>
  <p class="hours" style="top:175px">Monday - Friday at 5pm<br>Saturday at 5pm<br>Sunday from 2pm-8pm</p>

  <p class="abs club-name">Fairbrook Cedar Club</p>
  <svg class="abs pin" width="10" height="13" viewBox="0 0 10 13" aria-hidden="true"><path d="M5 12.5C2 8.5 1 6.8 1 5a4 4 0 0 1 8 0c0 1.8-1 3.5-4 7.5z" fill="none" stroke="#f9bd1b" stroke-width="1.5"/><circle cx="5" cy="5" r="1.4" fill="#f9bd1b"/></svg>
  <p class="abs address">Lodge# 4817<br>120 N Maple St<br>Fairbrook, KS 66700</p>
  <div class="abs back-phone">
    <svg width="15" height="15" viewBox="0 0 24 24" aria-hidden="true"><circle cx="12" cy="12" r="10.5" fill="none" stroke="#1d2a44" stroke-width="2"/><path d="M8.5 6.5l2 2.2-1.2 1.6a8 8 0 0 0 4.4 4.4l1.6-1.2 2.2 2-1.5 2c-4.6-.3-8.3-4-8.8-8.8z" fill="#1d2a44"/></svg>
    402-555-0147
  </div>

  <div class="photo" role="img" aria-label="Photo of a breaded chicken sandwich with fries" style="left:194px;top:49px;width:152px;height:152px;background:radial-gradient(circle,#d6a45c,#7b4a22 60%,#2a221c)"></div>
  <div class="dot" style="left:198px;top:164px;width:46px;height:46px;background:#8c2d5a;opacity:.8"></div>
  <div class="photo" role="img" aria-label="Photo of tater gems and fried mushrooms with ranch" style="left:214px;top:224px;width:184px;height:184px;background:radial-gradient(circle,#e0b86a,#b07a34 60%,#6a4420)"></div>
  <div class="dot" style="left:201px;top:360px;width:44px;height:44px;background:#f08a2a;opacity:.75"></div>
  <div class="photo" role="img" aria-label="Photo of a BLT sandwich" style="left:363px;top:303px;width:118px;height:118px;background:radial-gradient(circle,#e8dcc4,#9a7a4a 60%,#2a221c)"></div>
  <div class="dot" style="left:361px;top:397px;width:36px;height:36px;background:#5b86c4;opacity:.75"></div>

  <div class="coupon" style="top:24px"><span class="scissors">✂</span><div class="coupon-off">$2 OFF</div><div class="coupon-item">ANY SANDWICH</div></div>
  <div class="coupon" style="top:96px"><span class="scissors">✂</span><div class="coupon-off">$2 OFF</div><div class="coupon-item">ANY APPETIZER</div></div>

  <div class="abs badges" aria-label="Partner badges">
    <div class="abs" style="left:5px;top:5px;width:40px;height:29px;background:var(--navy)"></div>
    <div class="abs" style="left:64px;top:10px;width:22px;height:22px;border-radius:50%;border:1px solid var(--red)"></div>
  </div>
  <p class="abs follow">Find us on <span style="display:inline-block;width:8px;height:8px;border-radius:50%;background:var(--blue);vertical-align:-1px"></span><br><span class="url">linkhub.com/cedarclub4817</span></p>

  <div class="abs brand" style="left:606px;top:42px;width:60px;height:60px;font-size:12px">Cedar<br>Club</div>
  <div class="abs stamp"></div>
  <div class="abs addr-line" style="top:259px"></div>
  <div class="abs addr-line" style="top:302px"></div>
  <div class="abs addr-line" style="top:343px"></div>
</section>

</body>
</html>
```